ALL TEXT GRAPHICS RK May 2025 for Instagram

We are looking for a series of social media graphics for Instagram (new size: 4:5 (1080 x 1350 pixels) ratio that are ALL TEXT. We want the following quotes below on each graphic; one quote per graphic. AND, In very small letters at the bottom of each graphic, add @RKBexleyOnline
The look and feel of these graphics should be complimentary to the color palette attached below; but keep them simple. But the design is up to you; at the end of this document, I provided various samples of all text graphics that I like as examples.
women looking to lose weight

```html
<!DOCTYPE html>
<html lang="en">
<head>
<meta charset="utf-8">
<title>RK All Text Graphics – Instagram Series</title>
<link rel="stylesheet" href="https://fonts.googleapis.com/css2?family=Anton&family=Open+Sans:ital,wght@0,300;0,400;0,600;0,700;1,300;1,700;1,800&display=swap">
<style>
  :root {
    --page-bg: #efefef;
    --card-bg: #ffffff;
    --ink: #111111;
    --magenta-deep: #d4006c;
    --magenta-hot: #ff2f96;
    --apple-red: #e3161f;
    --scale-pink: #f04a86;
  }
  * { box-sizing: border-box; margin: 0; padding: 0; }
  html, body { width: 1200px; height: 1200px; overflow: hidden; }
  body {
    background: var(--page-bg);
    position: relative;
    font-family: "Open Sans", Arial, sans-serif;
    color: var(--ink);
  }
  .post {
    position: absolute;
    width: 259px;
    height: 324px;
    background: var(--card-bg);
    padding: 26px 18px 0 19px;
  }
  .headline {
    font-family: "Anton", Impact, sans-serif;
    font-weight: 400;
    line-height: 1.08;
    text-transform: uppercase;
    color: var(--magenta-deep);
    letter-spacing: -0.2px;
  }
  .headline .hot { color: var(--magenta-hot); }
  .headline .line { display: block; }
  .body-copy { font-weight: 300; line-height: 1.2; margin-top: 14px; }
  .body-copy strong { font-weight: 700; }
  .accent { color: var(--magenta-hot); }
  .accent-deep { color: var(--magenta-deep); }
  .cta {
    display: flex;
    align-items: center;
    gap: 12px;
    font-weight: 800;
    font-style: italic;
    margin-top: 14px;
  }
  .apple {
    display: inline-block;
    width: 38px;
    height: 36px;
    border-radius: 48% 48% 50% 50%;
    background: var(--apple-red);
    flex: none;
  }
  .scale-icon {
    display: inline-block;
    width: 60px;
    height: 40px;
    border-radius: 10px;
    background: linear-gradient(180deg, var(--scale-pink), #c81e5a);
    transform: skewX(-10deg);
    flex: none;
  }
  .handle {
    position: absolute;
    left: 19px;
    bottom: 22px;
    font-size: 9.5px;
    font-style: italic;
    font-weight: 400;
  }

  /* positions */
  .post--tired    { left: 37px;  top: 36px; }
  .post--weight   { left: 329px; top: 36px; }
  .post--hormonal { left: 620px; top: 36px; }
  .post--after40  { left: 911px; top: 36px; }
  .post--tummy    { left: 37px;  top: 439px; }
  .post--bloating { left: 327px; top: 439px; }
  .post--plan     { left: 617px; top: 439px; }
  .post--secret   { left: 907px; top: 439px; }
  .post--thirties { left: 36px;  top: 819px; }

  /* individual type sizes */
  .post--tired .l1 { font-size: 40px; }
  .post--tired .l2 { font-size: 27px; }
  .post--tired .body-copy { font-size: 29px; margin-top: 18px; }
  .post--tired .cta { font-size: 22px; }

  .post--weight .headline { font-size: 32px; }
  .post--weight .body-copy { font-size: 22px; line-height: 1.25; margin-top: 16px; }
  .post--weight .cta { font-size: 20px; color: var(--magenta-deep); }

  .post--hormonal .l1 { font-size: 23.5px; }
  .post--hormonal .l2 {
    font-family: "Open Sans", Arial, sans-serif;
    font-weight: 800; font-style: italic; text-transform: none;
    font-size: 24px; margin-top: 4px; color: var(--magenta-hot);
  }
  .post--hormonal .fix-lead { font-size: 22px; line-height: 1.2; margin-top: 20px; }
  .post--hormonal .fix-lead b { font-weight: 600; }
  .post--hormonal .fix-lead span { font-weight: 300; }
  .post--hormonal .comment { font-size: 17px; font-style: italic; font-weight: 300; line-height: 1.3; margin-top: 16px; }
  .post--hormonal .comment b { font-weight: 700; color: var(--magenta-deep); }

  .post--after40 .l1 { font-size: 36px; }
  .post--after40 .l2 { font-size: 27px; }
  .post--after40 .body-copy { font-size: 24px; line-height: 1.28; margin-top: 10px; }
  .post--after40 .cta { font-size: 20px; }

  .post--tummy .headline { font-size: 33px; line-height: 1.12; }
  .post--tummy .still { font-size: 30px; font-weight: 300; margin-top: 14px; }
  .post--tummy .still strong { font-weight: 700; }
  .post--tummy .comment { font-size: 20px; font-weight: 300; line-height: 1.25; margin-top: 14px; }
  .post--tummy .comment b { font-weight: 700; color: var(--magenta-hot); }

  .post--bloating .headline { font-size: 25px; }
  .post--bloating .body-copy { font-size: 24px; line-height: 1.25; margin-top: 22px; }
  .post--bloating .body-copy strong { font-weight: 600; }
  .post--bloating .body-copy .accent { font-weight: 600; }
  .post--bloating .cta { font-size: 20px; margin-top: 26px; gap: 24px; }
  .post--bloating .apple { width: 44px; height: 42px; }

  .post--plan .headline { font-size: 37px; line-height: 0.95; text-transform: none; }
  .post--plan .lead { font-size: 30px; font-weight: 300; line-height: 1.25; margin-top: 2px; }
  .post--plan .detail { font-size: 21px; font-weight: 400; line-height: 1.2; margin-top: 6px; }
  .post--plan .cta { font-size: 20px; margin-top: 8px; gap: 30px; }
  .post--plan .apple { width: 44px; height: 42px; }

  .post--secret .l1 { font-size: 29px; }
  .post--secret .l2 { font-size: 20px; line-height: 1.2; }
  .post--secret .body-copy { font-size: 25px; line-height: 1.2; margin-top: 20px; }
  .post--secret .apple { width: 32px; height: 30px; vertical-align: -4px; margin-left: 10px; }

  .post--thirties .headline { font-size: 33px; line-height: 1.1; }
  .post--thirties .body-copy { font-size: 25px; line-height: 1.2; margin-top: 14px; }
  .post--thirties .apple { width: 32px; height: 30px; vertical-align: -4px; margin-left: 12px; }
</style>
</head>
<body>

<article class="post post--tired">
  <h2 class="headline"><span class="line l1">Tired. <span class="hot">Moody.</span></span><span class="line l2 hot">Stubborn belly fat.</span></h2>
  <p class="body-copy">Your hormones<br>are screaming<br>for help!</p>
  <p class="cta">Let's fix that. <span class="scale-icon" role="img" aria-label="Pink bathroom scale illustration"></span></p>
  <p class="handle">@RKBexleyOnline</p>
</article>

<article class="post post--weight">
  <h2 class="headline"><span class="line">That stubborn</span><span class="line hot">weight?</span></h2>
  <p class="body-copy">It's not your fault.<br>Your <strong>hormones</strong> are<br>to blame and you're<br>not alone</p>
  <p class="cta">But there is a fix <span class="apple" role="img" aria-label="Red apple with scale dial illustration"></span></p>
  <p class="handle">@RKBexleyOnline</p>
</article>

<article class="post post--hormonal">
  <h2 class="headline"><span class="line l1">Your belly isn't fat...</span><span class="line l2">It's HORMONAL.</span></h2>
  <p class="fix-lead"><b>Here's how to fix it</b><br><span>but clean and<br>reassuring.</span></p>
  <p class="comment">Comment <b>HORMONES</b> if<br>nothing is working.</p>
  <p class="handle">@RKBexleyOnline</p>
</article>

<article class="post post--after40">
  <h2 class="headline"><span class="line l1">The stubborn</span><span class="line l2 hot">Belly fat after 40?</span></h2>
  <p class="body-copy">It's not about<br><strong>calories</strong><br>it's about your<br><strong class="accent-deep">hormones</strong>.</p>
  <p class="cta">Here is the fix! <span class="apple" role="img" aria-label="Red apple with scale dial illustration"></span></p>
  <p class="handle">@RKBexleyOnline</p>
</article>

<article class="post post--tummy">
  <h2 class="headline"><span class="line">Flat tummy</span><span class="line hot">in your 40s?</span></h2>
  <p class="still">It's still <strong>possible</strong></p>
  <p class="comment">Comment <b>BYE BELLY</b><br>to get the 10 secrets to<br>a flatter tummy</p>
  <p class="handle">@RKBexleyOnline</p>
</article>

<article class="post post--bloating">
  <h2 class="headline"><span class="line">Bloating. Muffin top.</span><span class="line hot">Puffy waistline.</span></h2>
  <p class="body-copy">Your body's<br><strong>screaming</strong> for a<br>different kind of <span class="accent-deep">fix</span>.</p>
  <p class="cta">Here it is <span class="apple" role="img" aria-label="Red apple with scale dial illustration"></span></p>
  <p class="handle">@RKBexleyOnline</p>
</article>

<article class="post post--plan">
  <h2 class="headline"><span class="line">This 90-day</span><span class="line">plan helped</span></h2>
  <p class="lead">women over 40<br>slim down</p>
  <p class="detail">get a <span class="accent">tiny waist</span> and<br>feel <span class="accent">sexy</span> again</p>
  <p class="cta">You're next <span class="apple" role="img" aria-label="Red apple with scale dial illustration"></span></p>
  <p class="handle">@RKBexleyOnline</p>
</article>

<article class="post post--secret">
  <h2 class="headline"><span class="line l1">This is the secret</span><span class="line l2 hot">Women over 40 are using<br>to get snatched</span></h2>
  <p class="body-copy">without starving.<br>Comment <span class="accent">SKINNY</span><br>to get the exact<br>plan <span class="apple" role="img" aria-label="Red apple with scale dial illustration"></span></p>
  <p class="handle">@RKBexleyOnline</p>
</article>

<article class="post post--thirties">
  <h2 class="headline"><span class="line">What worked in</span><span class="line">your 30s <span class="hot">won't</span></span><span class="line hot">work now</span></h2>
  <p class="body-copy">Here's what<br>actually does.<br><span class="accent">Drop 30 Pounds</span><br>in 3 Months <span class="apple" role="img" aria-label="Red apple with scale dial illustration"></span></p>
  <p class="handle">@RKBexleyOnline</p>
</article>

</body>
</html>
```